Palmcrest Shuttle & Excursions St. Lucia

I want a website design that is vibrant, engaging, and converts.
I plan on using Squarespace for hosting.

Target Market(s)

Tourists and visitors to St. Lucia; Focus: North American Market then European

Industry/Entity Type

Travel & Tourism

Coding

Coded - Design and coding required

Number of Pages Required

1 page

```html
<!DOCTYPE html>
<html lang="en">
<head>
<meta charset="utf-8">
<title>Palmcrest Shuttle &amp; Excursions St. Lucia</title>
<link href="https://fonts.googleapis.com/css2?family=Lora:wght@700&family=Lato:wght@400;700&display=swap" rel="stylesheet">
<style>
:root{
  --navy:#142c72;
  --navy-deep:#0f235c;
  --olive:#7b8f2f;
  --olive-soft:#8a9c3c;
  --ink:#2b2b2b;
  --muted:#555;
  --white:#fff;
  --gold:#e3a21a;
  --line:#d9d9d9;
}
*{margin:0;padding:0;box-sizing:border-box}
html,body{width:1200px;height:4815px;overflow:hidden}
body{position:relative;font-family:'Lato',sans-serif;color:var(--ink);background:var(--white)}
.abs{position:absolute}
.serif{font-family:'Lora',serif;font-weight:700}
.btn{position:absolute;display:flex;align-items:center;justify-content:center;border-radius:26px;font:700 13px 'Lato',sans-serif;letter-spacing:.2px;text-transform:uppercase}
.btn-outline{border:2px solid var(--olive);color:var(--navy);background:var(--white)}
.btn-olive{background:var(--olive);color:var(--white)}
.btn-navy{background:var(--navy);color:var(--white)}
.section-title{position:absolute;left:0;width:1200px;text-align:center;font-family:'Lora',serif;font-weight:700;font-size:46px;color:var(--navy);text-transform:uppercase;letter-spacing:.5px}
.section-title span{border-bottom:3px solid var(--navy);padding-bottom:2px}
/* header */
.brand{left:121px;top:38px;font-family:'Lora',serif;font-weight:700;font-size:26px;line-height:38px;color:var(--navy);text-transform:uppercase}
.phone{left:800px;top:40px;font-size:15px;color:var(--navy);display:flex;align-items:center;gap:8px}
.social{display:flex;gap:10px}
.social i{display:block;width:34px;height:34px;border-radius:50%;border:2px solid var(--olive)}
.social i.fill{background:var(--olive)}
.nav{left:469px;top:101px;display:flex;gap:31px;font-size:14px;font-weight:700;color:var(--navy);text-transform:uppercase}
.nav .active{color:var(--olive)}
/* hero */
.hero{left:0;top:146px;width:1200px;height:643px;background:linear-gradient(180deg,#7fb0d8 0%,#5e8f4a 30%,#3d6b2e 48%,#2f93b0 62%,#d9c9a0 80%,#1f6f9a 100%)}
.hero-title{left:0;top:356px;width:1200px;text-align:center;color:var(--white);font-size:60px;line-height:74px;text-transform:uppercase}
.dots{left:562px;top:740px;display:flex;gap:14px;align-items:center}
.dots i{width:6px;height:6px;border-radius:50%;background:var(--white)}
.dots i.on{width:22px;height:22px;border:2px solid var(--white);background:transparent;position:relative}
/* services */
.svc-ring{width:306px;height:306px;border-radius:50%;border:4px solid var(--navy);padding:10px}
.svc-ring.olive{border-color:var(--olive)}
.svc-ring div{width:100%;height:100%;border-radius:50%}
.svc-name{width:330px;text-align:center;font-size:19px;font-weight:700;color:var(--navy);text-transform:uppercase}
.svc-text{width:310px;text-align:center;font-size:15px;line-height:26px;color:var(--muted)}
.chev{color:var(--olive);font-size:38px;font-weight:700}
/* about */
.about{left:0;top:1619px;width:1200px;height:564px;background:var(--navy)}
.about-ring{left:112px;top:1684px;width:434px;height:434px;border-radius:50%;border:6px solid var(--olive);padding:14px}
.about-ring div{width:100%;height:100%;border-radius:50%;background:linear-gradient(180deg,#6fb2e6 0%,#aed4ee 45%,#e9eef0 65%,#3f8fb5 100%)}
.about h2{left:598px;top:1690px;font-size:44px;color:var(--white)}
.about h2 span{border-bottom:3px solid var(--white)}
.about p{left:598px;width:490px;font-size:15px;line-height:27px;color:var(--white);text-align:justify}
/* reviews */
.card{width:304px;height:275px;background:var(--white);box-shadow:0 4px 16px rgba(0,0,0,.12);padding:24px 22px}
.stars{color:var(--gold);font-size:15px;letter-spacing:2px}
.card p{font-size:15px;line-height:27px;color:var(--ink);margin-top:12px;padding-bottom:14px;border-bottom:1px solid var(--line)}
.who{display:flex;align-items:center;gap:18px;margin-top:20px}
.avatar{width:54px;height:54px;border-radius:50%;background:linear-gradient(135deg,#c9a88c,#7c5a44)}
.who b{display:block;font-size:14px;color:var(--navy);text-transform:uppercase}
.who small{font-size:12px;font-weight:700;color:var(--olive)}
.round-arrow{width:34px;height:34px;border-radius:50%;display:flex;align-items:center;justify-content:center;font-weight:700;font-size:18px}
/* enjoy band */
.enjoy{left:0;top:2770px;width:1200px;height:471px;background:linear-gradient(180deg,#7f953a 0%,#7b9236 50%,#88a03f 100%)}
.enjoy h2{left:0;top:2842px;width:1200px;text-align:center;font-size:38px;line-height:49px;color:var(--white);text-transform:uppercase}
.enjoy h2 span{border-bottom:3px solid var(--white)}
.enjoy p{left:130px;top:2969px;width:940px;text-align:center;font-size:15px;line-height:28px;color:var(--white)}
/* gallery */
.ph{position:absolute}
/* footer */
.footer{left:0;top:4205px;width:1200px;height:610px;background:var(--navy)}
.news{left:0;top:4254px;width:1200px;text-align:center;font-size:36px;color:var(--white);text-transform:uppercase}
.news span{border-bottom:3px solid var(--white)}
.email{left:209px;top:4342px;width:626px;height:48px;border:1.5px solid var(--white);border-radius:26px;color:var(--white);font-size:14px;padding-left:24px;display:flex;align-items:center}
.rule{left:112px;width:976px;height:1px;background:rgba(255,255,255,.25)}
.fcol h4{font-size:17px;font-weight:700;color:var(--white);text-transform:uppercase;margin-bottom:14px}
.fcol li{list-style:none;font-size:14px;color:var(--white);line-height:37.5px;display:flex;align-items:center;gap:20px}
.fcol li::before{content:"";width:6px;height:6px;border-radius:50%;background:var(--olive)}
.contact li{display:flex;gap:16px;font-size:14px;color:var(--white);line-height:22px;margin-bottom:16px;list-style:none}
.copy{left:0;top:4767px;width:1200px;text-align:center;font-size:13px;color:var(--white)}
</style>
</head>
<body>

<!-- Header -->
<div class="abs brand">Palmcrest Shuttle &amp;<br>Excursions St. Lucia</div>
<div class="abs phone">
  <svg width="14" height="14" viewBox="0 0 24 24"><path fill="#7b8f2f" d="M6.6 10.8a15 15 0 0 0 6.6 6.6l2.2-2.2c.3-.3.7-.4 1-.2 1.1.4 2.3.6 3.6.6.6 0 1 .4 1 1V20c0 .6-.4 1-1 1A17 17 0 0 1 3 4c0-.6.4-1 1-1h3.5c.6 0 1 .4 1 1 0 1.3.2 2.5.6 3.6.1.3 0 .7-.2 1z"/></svg>
  <span>+1 (758) 555 0142</span>
</div>
<div class="abs social" style="left:992px;top:33px"><i class="fill"></i><i></i><i></i><i></i></div>
<nav class="abs nav"><span class="active">Home</span><span>Tours</span><span>Transports</span><span>Gallery</span><span>Book a Tour</span><span>Reviews</span><span>Contact Us</span></nav>

<!-- Hero -->
<div class="abs hero" role="img" aria-label="Photo of a green volcanic peak rising over a turquoise bay with a sandy beach"></div>
<div class="abs hero-title serif">Palmcrest Shuttle &amp;<br>Excursions St. Lucia</div>
<div class="btn" style="left:492px;top:524px;width:216px;height:48px;background:var(--white);color:var(--navy)">Book an Adventure</div>
<div class="abs dots"><i></i><i class="on"></i><i></i><i></i></div>

<!-- Services -->
<div class="section-title" style="top:898px"><span>Services We Offer</span></div>
<div class="abs chev" style="left:40px;top:1130px">&#8249;</div>
<div class="abs chev" style="left:1136px;top:1130px">&#8250;</div>

<div class="abs svc-ring" style="left:112px;top:1004px"><div role="img" aria-label="Photo of two riders on ATVs in a rainforest" style="background:linear-gradient(160deg,#7c9a5a,#3e4f33)"></div></div>
<div class="abs svc-ring olive" style="left:447px;top:1004px"><div role="img" aria-label="Photo of a harbour town surrounded by green hills" style="background:linear-gradient(180deg,#9fc0d9,#6b8f60 45%,#4f86a0 75%,#5c7a4a)"></div></div>
<div class="abs svc-ring" style="left:780px;top:1004px"><div role="img" aria-label="Photo of a cruise ship beside palm trees under a blue sky" style="background:linear-gradient(180deg,#3e9fe0,#8ccbf0 55%,#e8f2f4 70%,#2aa6b5)"></div></div>

<div class="abs svc-name" style="left:100px;top:1345px">ATV Rainforest Adventures</div>
<div class="abs svc-name" style="left:435px;top:1345px">St. Lucia Car and Rental</div>
<div class="abs svc-name" style="left:768px;top:1345px">Cruise Ship Excursion</div>
<div class="abs svc-text" style="left:110px;top:1380px">Lorem ipsum dolor sit amet, consectetur adipiscing elit, sed do eiusmod tempor incididunt lab dolorea.</div>
<div class="abs svc-text" style="left:445px;top:1380px">Lorem ipsum dolor sit amet, consectetur adipiscing elit, sed do eiusmod tempor incididunt lab dolorea.</div>
<div class="abs svc-text" style="left:778px;top:1380px">Lorem ipsum dolor sit amet, consectetur adipiscing elit, sed do eiusmod tempor incididunt lab dolorea.</div>
<div class="btn btn-outline" style="left:194px;top:1478px;width:144px;height:48px">Read More</div>
<div class="btn btn-olive" style="left:529px;top:1478px;width:144px;height:48px">Read More</div>
<div class="btn btn-outline" style="left:862px;top:1478px;width:144px;height:48px">Read More</div>

<!-- About -->
<section class="abs about"></section>
<div class="abs about-ring"><div role="img" aria-label="Photo of a marina with sailboats and a palm tree"></div></div>
<h2 class="abs serif about" style="position:absolute;left:598px;top:1690px;width:auto;height:auto;background:none;font-size:44px;color:var(--white)"><span style="border-bottom:3px solid #fff">ABOUT US</span></h2>
<p class="abs" style="left:598px;top:1780px;width:490px;font-size:15px;line-height:27px;color:#fff;text-align:justify">Lorem ipsum dolor sit amet, consectetur adipiscing elit, sed do eiusmod tempor incididunt ut labore et dolore magna aliqua. Ut enim ad minim veniam, quis nostrud exercitation ullamco laboris nisi ut aliquip ex ea commodo consequat duis aute irure dolor in reprehe nderit in voluptate velit esse cillum dolorea.</p>
<p class="abs" style="left:598px;top:1935px;width:490px;font-size:15px;line-height:27px;color:#fff;text-align:justify">Lorem ipsum dolor sit amet, consectetur adipiscing elit, sed do eiusmod tempor incididunt ut labore et dolore magna aliqua. Ut enim ad minim veniam, quis nostrud exercitation ullamco.</p>
<div class="btn btn-olive" style="left:598px;top:2047px;width:148px;height:48px">Learn More</div>

<!-- Reviews -->
<div class="section-title" style="top:2296px"><span>Our Reviews</span></div>
<div class="abs round-arrow" style="left:35px;top:2517px;background:#eef0f4;color:var(--navy)">&#8249;</div>
<div class="abs round-arrow" style="left:1130px;top:2517px;background:var(--olive);color:#fff">&#8250;</div>

<div class="abs card" style="left:112px;top:2398px">
  <div class="stars">★★★★★</div>
  <p>Lorem ipsum dolor sit amet, consect adipiscing elit, sed do eiusmod temp incididunt ut labore et dolore magna t enim ad minim veniam.</p>
  <div class="who"><div class="avatar"></div><div><b>Marcus Hale</b><small>St. Lucia</small></div></div>
</div>
<div class="abs card" style="left:448px;top:2398px">
  <div class="stars">★★★★★</div>
  <p>Lorem ipsum dolor sit amet, consect adipiscing elit, sed do eiusmod temp incididunt ut labore et dolore magna t enim ad minim veniam.</p>
  <div class="who"><div class="avatar" style="background:linear-gradient(135deg,#8a6a52,#3c2a20)"></div><div><b>Priya</b><small>St. Lucia</small></div></div>
</div>
<div class="abs card" style="left:784px;top:2398px">
  <div class="stars">★★★★★</div>
  <p>Lorem ipsum dolor sit amet, consect adipiscing elit, sed do eiusmod temp incididunt ut labore et dolore magna t enim ad minim veniam.</p>
  <div class="who"><div class="avatar" style="background:linear-gradient(135deg,#bcbcbc,#6e6258)"></div><div><b>Marcus Hale</b><small>St. Lucia</small></div></div>
</div>

<!-- Enjoy band -->
<section class="abs enjoy" role="img" aria-label="Green-tinted photo of a person paddleboarding on calm water near a peak"></section>
<h2 class="abs serif" style="left:0;top:2842px;width:1200px;text-align:center;font-size:38px;line-height:49px;color:#fff">
  <span style="border-bottom:3px solid #fff">ENJOY AND EXPERIENCE</span><br><span style="border-bottom:3px solid #fff">ST LUCIA WITH US</span></h2>
<p class="abs" style="left:130px;top:2969px;width:940px;text-align:center;font-size:15px;line-height:28px;color:#fff">Lorem ipsum dolor sit amet, consectetur adipiscing elit, sed do eiusmod tempor incididunt ut labore et dolore magna aliqua. Ut enim ad minim veniam, quis nostrud exercitation ullamco laboris nisi ut aliquip ex ea commodo consequat duis aute irure dolor in reprehenderit in voluptate velit esse cillum doloconsectetur adipiscing elit, sed do eiusmod tempor incididunt ut labore et dolore magna enim ad minim veniam, quis nostrud exercitation ullamcoea.</p>
<div class="btn btn-navy" style="left:522px;top:3111px;width:156px;height:48px">Get in Touch</div>

<!-- Gallery -->
<div class="section-title" style="top:3360px"><span>Our Gallery</span></div>
<div class="ph" style="left:112px;top:3463px;width:479px;height:322px;background:linear-gradient(180deg,#5d8fd0,#b9d2e6 35%,#2f5a2c 60%,#d8cdb0 100%)" role="img" aria-label="Photo of a palm-lined beach with boats on the sand"></div>
<div class="ph" style="left:609px;top:3463px;width:479px;height:322px;background:linear-gradient(180deg,#a7c3d6,#6f8a5a 30%,#3b86b4 55%,#6fa8c9 100%)" role="img" aria-label="Photo of a bay with sailboats below green hills"></div>
<div class="ph" style="left:112px;top:3804px;width:314px;height:287px;background:linear-gradient(180deg,#8fb0a8,#4e7a3a 45%,#2f5a22 100%)" role="img" aria-label="Aerial photo of a green cove"></div>
<div class="ph" style="left:443px;top:3804px;width:314px;height:287px;background:linear-gradient(180deg,#6d6b72,#d3a880 40%,#4d6a5a 70%,#2d4a28 100%)" role="img" aria-label="Photo of a harbour at sunset with palm trees"></div>
<div class="ph" style="left:774px;top:3804px;width:314px;height:287px;background:linear-gradient(180deg,#7fb3de,#a9cde6 35%,#3f6e35 60%,#2c5220 100%)" role="img" aria-label="Photo of twin volcanic peaks over forest"></div>

<!-- Footer -->
<footer class="abs footer"></footer>
<div class="abs serif news"><span>Sign Up for Newsletter</span></div>
<div class="abs email">Enter Email Address</div>
<div class="btn btn-olive" style="left:845px;top:4342px;width:146px;height:48px">Sign Up</div>
<div class="abs rule" style="top:4430px"></div>

<div class="abs serif" style="left:112px;top:4570px;font-size:25px;line-height:38px;color:#fff;text-transform:uppercase">Palmcrest Shuttle &amp;<br>Excursions St. Lucia</div>

<div class="abs fcol" style="left:432px;top:4470px">
  <h4>Navigation</h4>
  <ul><li>Home</li><li>Tours</li><li>Transports</li><li>Gallery</li><li>Book A Tour</li><li>Reviews</li></ul>
</div>
<div class="abs fcol" style="left:592px;top:4470px">
  <h4>Quick Links</h4>
  <ul><li>FAQ</li><li>Contact Us</li><li>Privacy Policy</li><li>Terms Of Use</li></ul>
</div>
<div class="abs fcol" style="left:763px;top:4470px;width:340px">
  <h4>Contact Info</h4>
  <ul class="contact">
    <li><svg width="12" height="16" viewBox="0 0 12 16" style="flex:none;margin-top:3px"><path fill="#7b8f2f" d="M6 0a6 6 0 0 0-6 6c0 4.5 6 10 6 10s6-5.5 6-10a6 6 0 0 0-6-6zm0 8.5A2.5 2.5 0 1 1 6 3.5a2.5 2.5 0 0 1 0 5z"/></svg><span>12 Harbourview Road, Rodney Bay,<br>St. Lucia</span></li>
    <li><svg width="13" height="13" viewBox="0 0 24 24" style="flex:none;margin-top:4px"><path fill="#7b8f2f" d="M6.6 10.8a15 15 0 0 0 6.6 6.6l2.2-2.2c.3-.3.7-.4 1-.2 1.1.4 2.3.6 3.6.6.6 0 1 .4 1 1V20c0 .6-.4 1-1 1A17 17 0 0 1 3 4c0-.6.4-1 1-1h3.5c.6 0 1 .4 1 1 0 1.3.2 2.5.6 3.6.1.3 0 .7-.2 1z"/></svg><span>+1 (758) 555 0142</span></li>
    <li><svg width="14" height="11" viewBox="0 0 14 11" style="flex:none;margin-top:5px"><rect width="14" height="11" rx="1.5" fill="#7b8f2f"/><path d="M1 1.5l6 4.5 6-4.5" stroke="#142c72" stroke-width="1.3" fill="none"/></svg><span>hello@palmcrestshuttle.com</span></li>
  </ul>
</div>

<div class="abs rule" style="top:4740px"></div>
<div class="abs copy">© 2023 <b>PALMCREST SHUTTLE &amp; EXCURSIONS ST. LUCIA</b> &nbsp;|&nbsp; All Rights Reserved</div>
<div class="abs social" style="left:924px;top:4755px"><i class="fill"></i><i></i><i></i><i></i></div>

</body>
</html>
```